Letterhead

Can you please design me a letterhead that I can use electronically in word as a template. I have attached my business card as I would like the design to reflect this logo.

```html
<!DOCTYPE html>
<html lang="en">
<head>
<meta charset="utf-8">
<title>Meridale Stationery</title>
<link rel="stylesheet" href="https://fonts.googleapis.com/css2?family=Open+Sans:wght@400;600&family=Arimo:wght@400&display=swap">
<style>
  :root {
    --board: #6b6c70;
    --paper: #ffffff;
    --brand-red: #b5202a;
    --brand-black: #0d0d0d;
    --ink: #3d3d3f;
    --ink-dark: #111111;
    --corner-tint: #f6dfe0;
    --corner-fade: rgba(246, 223, 224, 0);
    --card-dark: #121011;
    --mark-dim: #7a1d22;
  }
  * { box-sizing: border-box; margin: 0; padding: 0; }
  html, body { width: 1200px; height: 900px; overflow: hidden; }
  body {
    position: relative;
    background: var(--board);
    font-family: "Open Sans", Arial, sans-serif;
    color: var(--ink);
  }

  /* Letterhead */
  .letterhead {
    position: absolute;
    left: 17px; top: 22px;
    width: 646px; height: 862px;
    background: var(--paper);
    box-shadow: 2px 3px 6px rgba(0,0,0,0.35);
  }
  .corner-accent { position: absolute; }
  .corner-accent.top-left { left: 0; top: 0; }
  .corner-accent.bottom-right { right: 0; bottom: 0; }

  .letterhead .brand { position: absolute; left: 226px; top: 12px; }
  .brand-name {
    font-family: "Open Sans", Arial, sans-serif;
    font-weight: 600;
    color: var(--brand-red);
    line-height: 1;
    letter-spacing: 0;
  }
  .letterhead .brand-name { font-size: 47px; }
  .brand-tagline {
    font-family: "Arimo", Arial, sans-serif;
    color: var(--ink-dark);
    white-space: nowrap;
  }
  .letterhead .brand-tagline { font-size: 11.5px; margin-top: 5px; margin-left: 2px; }

  .band { position: absolute; display: flex; }
  .band .band-red { background: var(--brand-red); }
  .band .band-black { background: var(--brand-black); }
  .letterhead .band { left: 0; top: 91px; width: 646px; height: 9px; }
  .letterhead .band-red { width: 556px; }
  .letterhead .band-black { flex: 1; }

  .contact-line { white-space: nowrap; color: var(--ink); }
  .contact-line .label, .contact-line .sep { color: var(--brand-red); }
  .letterhead .contact-line {
    position: absolute; top: 108px; left: 0; width: 100%;
    text-align: center; font-size: 13.5px; word-spacing: -1px;
  }

  /* Business cards */
  .card {
    position: absolute; left: 703px; width: 370px; height: 228px;
    box-shadow: 3px 4px 7px rgba(0,0,0,0.4);
    overflow: hidden;
  }
  .card-front { top: 158px; background: var(--paper); }
  .card-front .brand { position: absolute; left: 90px; top: 56px; }
  .card-front .brand-name { font-size: 42px; }
  .card-front .brand-tagline { font-size: 10.5px; margin-top: 6px; margin-left: 3px; }
  .card-front .holder {
    position: absolute; left: 37px; top: 164px;
    font-size: 11px; white-space: nowrap;
  }
  .holder .holder-name { font-weight: 600; color: var(--ink); }
  .holder .sep { color: var(--brand-red); margin: 0 2px; }
  .holder .holder-role { color: var(--brand-red); font-size: 10px; }
  .card-front .contact-line {
    position: absolute; left: 38px; top: 180px; font-size: 9.5px; word-spacing: -1px;
  }
  .card-front .band { left: 0; bottom: 0; width: 100%; height: 23px; }
  .card-front .band-red { width: 319px; }
  .card-front .band-black { flex: 1; }

  .card-back {
    top: 402px;
    background: radial-gradient(ellipse at 50% 48%, #2c2627 0%, #1a1617 45%, var(--card-dark) 100%);
    display: flex; align-items: center; justify-content: center;
  }
  .card-back .brand-name { font-size: 54px; color: var(--mark-dim); margin-top: 6px; }
</style>
</head>
<body>

  <section class="letterhead" aria-label="Letterhead">
    <svg class="corner-accent top-left" width="186" height="186" viewBox="0 0 186 186" role="img" aria-label="Diagonal line accent in pale red and grey">
      <defs>
        <linearGradient id="fadeTopLeft" x1="0" y1="0" x2="1" y2="1">
          <stop offset="0" stop-color="var(--corner-tint)"/>
          <stop offset="0.5" stop-color="var(--corner-fade)"/>
        </linearGradient>
      </defs>
      <polygon points="0,0 186,0 0,186" fill="url(#fadeTopLeft)"/>
    </svg>

    <svg class="corner-accent bottom-right" width="146" height="146" viewBox="0 0 146 146" role="img" aria-label="Diagonal line accent in pale red">
      <defs>
        <linearGradient id="fadeBottomRight" x1="1" y1="1" x2="0" y2="0">
          <stop offset="0" stop-color="var(--corner-tint)"/>
          <stop offset="0.5" stop-color="var(--corner-fade)"/>
        </linearGradient>
      </defs>
      <polygon points="146,0 146,146 0,146" fill="url(#fadeBottomRight)"/>
    </svg>

    <div class="brand">
      <div class="brand-name">meridale</div>
      <div class="brand-tagline">Business Consultants Pty Ltd</div>
    </div>

    <div class="band"><span class="band-red"></span><span class="band-black"></span></div>

    <p class="contact-line">
      <span class="label">P</span> : 0412 555 018 <span class="sep">|</span>
      <span class="label">E</span> : helena@meridale.net.au <span class="sep">|</span>
      <span class="label">ACN</span> : 012 345 678
    </p>
  </section>

  <section class="card card-front" aria-label="Business card front">
    <div class="brand">
      <div class="brand-name">meridale</div>
      <div class="brand-tagline">Business Consultants Pty Ltd</div>
    </div>
    <p class="holder">
      <span class="holder-name">Helena Marsh</span> <span class="sep">|</span> <span class="holder-role">Principal</span>
    </p>
    <p class="contact-line">
      <span class="label">P</span> : 0412 555 018 <span class="sep">|</span>
      <span class="label">E</span> : helena@meridale.net.au <span class="sep">|</span>
      <span class="label">ACN</span> : 012 345 678
    </p>
    <div class="band"><span class="band-red"></span><span class="band-black"></span></div>
  </section>

  <section class="card card-back" aria-label="Business card back">
    <div class="brand-name">meridale</div>
  </section>

</body>
</html>
```